Facebook Ad For New online Spectacle Store

We have started a new online store in Australia selling spectacles. As we don't have overheads such as rent electricity etc we are able to do these glasses at an extremely cheap price of $50 for the complete pair. We want to highlight the affordability and quality. This ad will be promoted on Facebook all over Australia. We want to make an impression. There are a lot of people wearing cheap magnifiers from chemists etc that are not suitable as most people need a corrective lens and rarely are both eyes the same power. So it's the people that are buying the $10 glasses we really want to sway to get ones that actually are the correct prescription for them without paying hundreds of dollars on a pair. "Throw away your magnifiers" As it's Facebook we can't really have too much writing in the image HOWEVER we want to highlight COMPLETE GLASSES $50 and that they will be the customers exact power lens. Our Website is www.lumavue.com.au I have uploaded our logo but you do not need it in the design. We will be adding text to the Ad but not in the image you design (except for complete glasses for $50). you can take some of the images of frames from the website or I can upload just ask- tell me which one suits your design. Basically you have freedom to come up with something that will impress our potential customers make them click the link and check out our website.

Target Market(s)

People that use Cheap magnifiers - our glasses are a upgrade and better for their eyes

Industry/Entity Type

Eyewear

Colors

Designer to choose colors to be used in the design.

Requirements
Must have
• Complete Glasses $50 (Plus postage)- The (plus postage) in smaller writing than the Complete glasses for $50 part

```html
<!DOCTYPE html>
<html lang="en">
<head>
<meta charset="utf-8">
<title>Complete Glasses $50 – Ad Set</title>
<link href="https://fonts.googleapis.com/css2?family=Bebas+Neue&display=swap" rel="stylesheet">
<style>
  :root {
    --board: #7d7b7c;
    --teal: #33afbb;
    --white: #ffffff;
    --ink: #000000;
    --base-dark: #4a4a4a;
  }
  * { margin: 0; padding: 0; box-sizing: border-box; }
  html, body { width: 1200px; height: 1200px; overflow: hidden; }
  body { background: var(--board); position: relative; font-family: "Bebas Neue", "Arial Narrow", sans-serif; }

  .ad { position: absolute; box-shadow: 0 6px 14px rgba(0,0,0,0.35); }

  /* square ad */
  .ad--square { left: 344px; top: 58px; width: 512px; height: 576px; background: var(--base-dark); }
  .ad--square .ad__face { position: absolute; left: 0; top: 0; width: 512px; height: 548px; background: var(--teal); }

  .headline {
    position: absolute; color: var(--white); font-size: 71px; line-height: 1;
    font-weight: 400; white-space: nowrap; text-align: center;
  }
  .price-box { position: absolute; background: var(--white); display: flex; align-items: center; justify-content: center; }
  .price { color: var(--ink); font-size: 268px; line-height: 1; padding-top: 22px; }

  .terms {
    position: absolute; left: 0; width: 100%; color: var(--white);
    font-weight: 400; line-height: 1; text-align: center; white-space: nowrap; letter-spacing: 1px;
  }
  .terms__postage { opacity: 0.85; }

  .ad--square .headline { left: 58px; top: 30px; width: 398px; }
  .ad--square .price-box { left: 58px; top: 100px; width: 398px; height: 239px; }
  .ad--square .terms { top: 552px; font-size: 20px; }

  .frames-photo { position: absolute; }
  .ad--square .frames-photo--round { left: 24px; top: 366px; width: 290px; height: 115px;
    background: radial-gradient(ellipse at center, rgba(43,52,102,0.55), rgba(43,52,102,0) 70%); }
  .ad--square .frames-photo--aviator { left: 262px; top: 450px; width: 232px; height: 90px;
    background: radial-gradient(ellipse at center, rgba(200,182,151,0.6), rgba(200,182,151,0) 70%); }

  /* wide ad */
  .ad--wide { left: 92px; top: 682px; width: 960px; height: 480px; background: var(--white); }
  .ad--wide .ad__panel { position: absolute; left: 458px; top: 0; width: 502px; height: 430px; background: var(--teal); }
  .ad--wide .ad__band { position: absolute; left: 458px; top: 430px; width: 502px; height: 50px; background: var(--ink); }
  .ad--wide .headline { left: 44px; top: 68px; width: 398px; }
  .ad--wide .price-box { left: 44px; top: 152px; width: 399px; height: 240px; }
  .ad--wide .terms { top: 13px; font-size: 26px; }
  .ad--wide .frames-photo--round { left: 40px; top: 62px; width: 384px; height: 160px;
    background: linear-gradient(180deg, #3b4478 0%, #8a7f78 60%, #f2f2f2 100%); opacity: 0.35; border-radius: 40% / 50%; }
  .ad--wide .frames-photo--aviator { left: 40px; top: 262px; width: 384px; height: 150px;
    background: linear-gradient(180deg, #d8cbb2 0%, #efe7da 100%); opacity: 0.7; border-radius: 30% / 50%; }
</style>
</head>
<body>
  <section class="ad ad--square">
    <div class="ad__face">
      <h1 class="headline">Complete Glasses</h1>
      <div class="price-box"><span class="price">$50</span></div>
      <div class="frames-photo frames-photo--round" role="img" aria-label="Navy round acetate spectacle frames with tortoiseshell arms"></div>
      <div class="frames-photo frames-photo--aviator" role="img" aria-label="Gold stainless steel aviator spectacle frames"></div>
    </div>
    <p class="terms"><span class="terms__postage">(Plus postage)</span> · Your exact prescription lenses</p>
  </section>

  <section class="ad ad--wide">
    <div class="frames-photo frames-photo--round" role="img" aria-label="Navy round acetate spectacle frames with tortoiseshell arms"></div>
    <div class="frames-photo frames-photo--aviator" role="img" aria-label="Gold stainless steel aviator spectacle frames"></div>
    <div class="ad__panel">
      <h1 class="headline">Complete Glasses</h1>
      <div class="price-box"><span class="price">$50</span></div>
    </div>
    <div class="ad__band">
      <p class="terms"><span class="terms__postage">(Plus postage)</span> · Your exact prescription lenses</p>
    </div>
  </section>
</body>
</html>
```